International Hand & Body company needing a Hand cream tube design for the Retail market

I am wanting a modern design for a new range of 6 hand creams I will be launching in August. They need to compliment our range of wrapped soaps which you can see on www.plovane.com.au so am wanting clean designs. I am wanting a solid colour with a hand drawn organic feel line drawing in black elegantly placed wrapping around the label. I am wanting to focus on the colour and positioning of words and fonts. I like modern clean contemporary fonts. The final design needs to appeal to the broader female market.This may lead to range expansion if designs are well received.
Updates

These designs are not hitting the brief. They are too generic and look like a supermarket brand. Our brand is more boutique and this design needs to be modern and simple. I would like more solid colours and more modern designs. Without patterns.

Target Market(s)

Female aged 20 - 70

Requirements
Must have
• a modern contemporary design that will appeal to the masses.
• Please read attached brief.
Should not have
• a black botanical illustration, in a loose and organic design to match the fragrance.

```html
<!DOCTYPE html>
<html lang="en">
<head>
<meta charset="utf-8">
<title>Plovane Hand Cream Range</title>
<link href="https://fonts.googleapis.com/css2?family=Josefin+Sans:wght@200;300;600&display=swap" rel="stylesheet">
<style>
  :root{
    --bg:#e9e5d3;
    --tube:#ffffff;
    --crimp:#f3f3f1;
    --cap:#e4e4e4;
    --ink:#2b2b2b;
    --muted:#555555;
    --yellow:#e8cc2a;
    --green:#97b87a;
    --blue:#5a9fd6;
    --pink:#e2959e;
    --orange:#d86c4c;
  }
  *{box-sizing:border-box;margin:0;padding:0}
  html,body{width:1200px;height:1200px;overflow:hidden}
  body{background:var(--bg);font-family:"Josefin Sans",sans-serif;color:var(--ink);position:relative}

  .front-row{position:absolute;top:50px;left:65px;display:flex;gap:30px}
  .back-row{position:absolute;top:730px;left:0;width:1200px;display:flex;justify-content:center;gap:40px}

  .tube{display:flex;flex-direction:column;align-items:center}
  .tube-body{position:relative;width:190px;height:580px;background:var(--tube);border-radius:4px 4px 2px 2px;box-shadow:0 2px 10px rgba(0,0,0,.08);overflow:hidden}
  .tube-body::before{content:"";position:absolute;top:0;left:0;right:0;height:16px;background:var(--crimp)}
  .tube-cap{width:150px;height:70px;background:var(--cap);border-radius:0 0 8px 8px}

  .band{position:absolute;top:0;left:40%;width:52%;height:150px;background:var(--c);display:flex;align-items:flex-end;justify-content:center;padding-bottom:14px}
  .brand{font-weight:600;font-size:17px;letter-spacing:2px;color:var(--ink);text-transform:lowercase}

  .fragrance{position:absolute;top:168px;left:26%;height:250px;writing-mode:vertical-rl;transform:rotate(180deg);text-align:end;font-weight:200;font-size:33px;line-height:36px;text-transform:uppercase;color:var(--ink);letter-spacing:-.5px}

  .product-type{position:absolute;bottom:0;left:18%;width:60%;height:82px;background:var(--c);color:#fff;font-weight:300;font-size:20px;line-height:19px;display:flex;flex-direction:column;align-items:center;justify-content:center;text-transform:uppercase}

  .yellow{--c:var(--yellow)} .green{--c:var(--green)} .blue{--c:var(--blue)} .pink{--c:var(--pink)} .orange{--c:var(--orange)}

  /* back of pack */
  .back .tube-body{width:170px;height:380px}
  .back .tube-cap{width:134px;height:52px}
  .back .band{left:30%;width:40%;height:72px;padding-bottom:8px}
  .back .brand{font-size:11px;letter-spacing:1.5px}
  .back-info{position:absolute;top:80px;left:14px;right:14px;font-size:6px;line-height:8px;color:var(--muted)}
  .back-info .origin{text-align:center;font-weight:600;margin-bottom:10px}
  .claims{list-style:none;text-align:right;margin-bottom:8px}
  .claims li::before{content:"• "}
  .ingredients{text-align:right;margin-bottom:10px}
  .ingredients b{font-weight:600;color:var(--ink)}
  .warning{text-align:right;font-weight:600;margin-bottom:8px}
  .directions{text-align:right;margin-bottom:30px}
  .skin{text-align:center;font-weight:600;margin-bottom:4px}
  .icons{display:flex;justify-content:center;gap:4px;margin-bottom:4px}
  .icons span{width:8px;height:8px;border:1px solid var(--muted);border-radius:2px}
  .contact{text-align:center}
</style>
</head>
<body>

<section class="front-row">
  <article class="tube yellow">
    <div class="tube-body">
      <div class="band"><span class="brand">plovane</span></div>
      <h2 class="fragrance">Other<br>Fragancy</h2>
      <div class="product-type"><span>Hand</span><span>Cream</span></div>
    </div>
    <div class="tube-cap"></div>
  </article>
  <article class="tube green">
    <div class="tube-body">
      <div class="band"><span class="brand">plovane</span></div>
      <h2 class="fragrance">Yuzu &amp;<br>Sage</h2>
      <div class="product-type"><span>Hand</span><span>Cream</span></div>
    </div>
    <div class="tube-cap"></div>
  </article>
  <article class="tube blue">
    <div class="tube-body">
      <div class="band"><span class="brand">plovane</span></div>
      <h2 class="fragrance">Citrus &amp;<br>Seagrass</h2>
      <div class="product-type"><span>Hand</span><span>Cream</span></div>
    </div>
    <div class="tube-cap"></div>
  </article>
  <article class="tube pink">
    <div class="tube-body">
      <div class="band"><span class="brand">plovane</span></div>
      <h2 class="fragrance">Fig &amp;<br>Sandalwood</h2>
      <div class="product-type"><span>Hand</span><span>Cream</span></div>
    </div>
    <div class="tube-cap"></div>
  </article>
  <article class="tube orange">
    <div class="tube-body">
      <div class="band"><span class="brand">plovane</span></div>
      <h2 class="fragrance">Other<br>Fragancy</h2>
      <div class="product-type"><span>Hand</span><span>Cream</span></div>
    </div>
    <div class="tube-cap"></div>
  </article>
</section>

<section class="back-row">
  <article class="tube back green">
    <div class="tube-body">
      <div class="band"><span class="brand">plovane</span></div>
      <div class="back-info">
        <p class="origin">MADE IN AUSTRALIA<br>36mL ℮ 1.18 fl. oz.</p>
        <ul class="claims"><li>No Sulfates</li><li>No Parabens</li><li>No Mineral Oils</li><li>No Artificial Colours</li></ul>
        <p class="ingredients"><b>INGREDIENTS:</b> Aqua, shea butter, glycerin, sweet almond oil, cetyl alcohol, jojoba oil, vitamin E, fragrance.</p>
        <p class="warning">DISCONTINUE USE IF IRRITATION OCCURS. KEEP AWAY FROM CHILDREN. AVOID CONTACT WITH EYES.</p>
        <p class="directions">MASSAGE INTO CLEAN DRY SKIN AS NEEDED.</p>
        <p class="skin">SUITABLE FOR ALL SKIN TYPES</p>
        <div class="icons"><span></span><span></span><span></span><span></span><span></span></div>
        <p class="contact">Unit 4, 12 Harbour Lane, Melbourne VIC 3000<br>www.plovane.com.au | sales@plovane.com.au</p>
      </div>
    </div>
    <div class="tube-cap"></div>
  </article>
  <article class="tube back blue">
    <div class="tube-body">
      <div class="band"><span class="brand">plovane</span></div>
      <div class="back-info">
        <p class="origin">MADE IN AUSTRALIA<br>36mL ℮ 1.18 fl. oz.</p>
        <ul class="claims"><li>No Sulfates</li><li>No Parabens</li><li>No Mineral Oils</li><li>No Artificial Colours</li></ul>
        <p class="ingredients"><b>INGREDIENTS:</b> Aqua, shea butter, glycerin, sweet almond oil, cetyl alcohol, jojoba oil, vitamin E, fragrance.</p>
        <p class="warning">DISCONTINUE USE IF IRRITATION OCCURS. KEEP AWAY FROM CHILDREN. AVOID CONTACT WITH EYES.</p>
        <p class="directions">MASSAGE INTO CLEAN DRY SKIN AS NEEDED.</p>
        <p class="skin">SUITABLE FOR ALL SKIN TYPES</p>
        <div class="icons"><span></span><span></span><span></span><span></span><span></span></div>
        <p class="contact">Unit 4, 12 Harbour Lane, Melbourne VIC 3000<br>www.plovane.com.au | sales@plovane.com.au</p>
      </div>
    </div>
    <div class="tube-cap"></div>
  </article>
  <article class="tube back pink">
    <div class="tube-body">
      <div class="band"><span class="brand">plovane</span></div>
      <div class="back-info">
        <p class="origin">MADE IN AUSTRALIA<br>36mL ℮ 1.18 fl. oz.</p>
        <ul class="claims"><li>No Sulfates</li><li>No Parabens</li><li>No Mineral Oils</li><li>No Artificial Colours</li></ul>
        <p class="ingredients"><b>INGREDIENTS:</b> Aqua, shea butter, glycerin, sweet almond oil, cetyl alcohol, jojoba oil, vitamin E, fragrance.</p>
        <p class="warning">DISCONTINUE USE IF IRRITATION OCCURS. KEEP AWAY FROM CHILDREN. AVOID CONTACT WITH EYES.</p>
        <p class="directions">MASSAGE INTO CLEAN DRY SKIN AS NEEDED.</p>
        <p class="skin">SUITABLE FOR ALL SKIN TYPES</p>
        <div class="icons"><span></span><span></span><span></span><span></span><span></span></div>
        <p class="contact">Unit 4, 12 Harbour Lane, Melbourne VIC 3000<br>www.plovane.com.au | sales@plovane.com.au</p>
      </div>
    </div>
    <div class="tube-cap"></div>
  </article>
</section>

</body>
</html>
```